K.L. Music Studio-Website
Music. Lessons. Recording.
K.L. Music Studio-Website -
Creative Brief
klmusicstudio.com
My name is Kevin Lorne and I am a musician, teacher and recording engineer. I started K.L. Music Studio so we can expand. We teach lessons in our students homes and in our studios. We offer lessons on a variety of instruments. We also provide musicians for performances, events, parties and more. We also have recording and producing capabilities.
K.L. Music Studio. Music. Lessons. Recording.
Like:Classy and stylish Clean and Simple Cool Cutting Edge Font: Simple, Clean-see Logo design page Want to Upload Videos Dislike: Too animated Too Cheesy Too Plain
Blue
Black/White
brambletonetunes.com
http://velvetkeysaudio.net/
http://mirokvenhal.com/
Thank you for your time!!! I recently had a logo made and would like the site to have that on display. I hope you underdstand what I'm going for. I need more students and want to advertise. I want it to be easy to navigate and draw peoples interest. I need to be able to upload videos. Clean and sophisticated. Cutting edge technology mixed with ancient instrument antiquity. I play violin and love to DJ if that helps. Please use the other websites as reference but I will leave it up to you. Let me know if you have questions and please stay in contact with me! Thank you so much for your time and work!!!!

```html
<!DOCTYPE html>
<html lang="en">
<head>
<meta charset="utf-8">
<title>K.L. Music Studio</title>
<link href="https://fonts.googleapis.com/css2?family=Arimo:wght@400;700&display=swap" rel="stylesheet">
<style>
:root{
  --bg-dark:#1c1c1c;
  --panel:#2a2a2a;
  --red:#e0141a;
  --red-dark:#a50b0f;
  --white:#ffffff;
  --social:#6a7fa6;
  --social-alt:#e27d22;
}
*{margin:0;padding:0;box-sizing:border-box}
html,body{width:1200px;height:969px;overflow:hidden}
body{
  position:relative;
  background:radial-gradient(ellipse at 50% 40%,#5a5a5a 0%,#383838 45%,#202020 100%);
  font-family:"Arimo",Arial,sans-serif;color:var(--white);
}
.main-nav{
  position:absolute;left:380px;top:8px;width:660px;height:42px;
  background:linear-gradient(#3c3c3c,#161616);border-radius:4px;
  display:flex;align-items:center;justify-content:space-around;font-size:15px;
}
.main-nav a{color:var(--white);text-decoration:none;padding:12px 26px}
.main-nav a.active{background:linear-gradient(#ff2a2a,var(--red-dark));border-radius:3px;margin-top:-6px;padding-top:18px}
.site-header{
  position:absolute;left:97px;top:52px;width:1006px;height:153px;
  background:linear-gradient(#2a2a2a,#0e0e0e);border-radius:8px;box-shadow:0 2px 6px #000;
}
.brand{position:absolute;left:36px;top:54px;display:flex;align-items:center;gap:14px}
.brand-mark{width:40px;height:40px;background:var(--white)}
.brand-name{font-family:"Arimo",Arial,sans-serif;font-weight:700;font-size:36px;color:var(--white)}
.follow{position:absolute;right:22px;top:0;background:var(--red);color:var(--white);font-size:15px;padding:3px 18px;letter-spacing:1px}
.social{position:absolute;right:22px;top:38px;display:flex;gap:9px}
.social span{width:36px;height:36px;border-radius:5px;background:var(--social)}
.social span:nth-child(4){background:var(--social-alt)}
.call{position:absolute;right:22px;top:100px;background:var(--red);border:2px solid #222;padding:9px 14px;font-size:19px;display:flex;align-items:center;gap:10px}
.hero{
  position:absolute;left:97px;top:215px;width:1006px;height:284px;
  background:linear-gradient(#3a3a3a,#111);border-radius:8px;overflow:hidden;
}
.hero-title{position:absolute;left:28px;top:44px;width:440px;font-family:"Arimo",Arial,sans-serif;font-weight:700;font-size:50px;line-height:58px;color:var(--white)}
.hero-tag{position:absolute;left:28px;top:190px;font-size:15px}
.btn{display:inline-block;background:linear-gradient(#ff3030,var(--red-dark));color:var(--white);border-radius:10px;font-size:14px;padding:5px 18px;text-decoration:none}
.hero .btn{position:absolute;left:32px;top:230px}
.hero-photo{position:absolute;left:493px;top:0;width:513px;height:284px;background:linear-gradient(135deg,#d8d2c6,#7a7368 60%,#2c2925)}
.lessons{
  position:absolute;left:97px;top:512px;width:607px;height:368px;
  background:linear-gradient(#444,#2c2c2c);border-radius:6px;
}
.lessons h2{position:absolute;left:10px;top:8px;font-weight:400;font-size:32px;color:var(--red)}
.lessons .body{position:absolute;left:10px;top:62px;width:405px;font-size:13px;line-height:15px}
.lessons .body p{margin-bottom:15px}
.lessons .body strong{color:var(--red);font-weight:400}
.lessons-photo{position:absolute;left:428px;top:13px;width:163px;height:342px;border:3px solid #bbb;border-radius:8px;background:linear-gradient(160deg,#8a6a4a,#2d2a2a 55%,#567)}
.side{position:absolute;left:714px;width:389px;background:linear-gradient(#444,#222);border-radius:6px}
.side h3{font-weight:400;font-size:26px;color:var(--red);margin:8px 10px 4px}
.side p{font-size:13px;line-height:15px;margin:0 10px;color:var(--white)}
.side .more{position:absolute;right:10px;bottom:8px;width:0;height:0;border-left:14px solid var(--red);border-top:8px solid transparent;border-bottom:8px solid transparent}
.about{top:512px;height:117px}
.news{top:638px;height:122px}
.watch{top:769px;height:111px}
.watch-video{position:absolute;left:4px;top:4px;width:210px;height:103px;background:linear-gradient(#6a6a6a,#1a1a1a);border:1px solid #888}
.watch-info{position:absolute;left:222px;top:0;width:160px}
.watch-info h3{margin:6px 0 2px;font-size:20px}
.watch-info p{margin:0;font-size:12px;line-height:14px}
.watch .btn{position:absolute;right:8px;bottom:6px;font-size:12px;padding:3px 12px}
.site-footer{
  position:absolute;left:97px;top:893px;width:1006px;height:57px;
  background:linear-gradient(#2e2e2e,#111);border-radius:6px;
  display:flex;align-items:center;justify-content:space-between;padding:0 10px;font-size:13px;
}
.site-footer nav a{color:var(--white);text-decoration:none}
.site-footer nav span{margin:0 14px}
</style>
</head>
<body>
<nav class="main-nav">
  <a class="active" href="#">Home</a><a href="#">About Us</a><a href="#">Lesson</a><a href="#">Give Back</a><a href="#">Contact Us</a>
</nav>

<header class="site-header">
  <div class="brand"><span class="brand-mark"></span><span class="brand-name">K.L. Music Studio</span></div>
  <div class="follow">Follow Us</div>
  <div class="social" aria-label="Social links"><span></span><span></span><span></span><span></span></div>
  <div class="call">
    <svg width="18" height="22" viewBox="0 0 18 22"><rect x="2" y="1" width="14" height="20" rx="2" fill="none" stroke="#fff" stroke-width="2"/><rect x="6" y="16" width="6" height="2" fill="#fff"/></svg>
    Call Us:111-111-1111
  </div>
</header>

<section class="hero">
  <h1 class="hero-title">K.L. Music Studio</h1>
  <p class="hero-tag">We teach lessons in our students homes and in our studios</p>
  <a class="btn" href="#">Click Here</a>
  <div class="hero-photo" role="img" aria-label="Photo of a cassette recorder and headphones on sheet music"></div>
</section>

<section class="lessons">
  <h2>Lessons</h2>
  <div class="body">
    <p><strong>We teach lessons in our students</strong><br>homes and in our studios. We offer lessons on a variety of instruments. We also provide musicians for performances, events, parties and more. We also have recording and producing capabilities.</p>
    <p>We teach lessons in our students <strong>homes and in our studios.</strong> We offer lessons on a variety of instruments. We also provide musicians for performances, events, parties and more. We also have recording and producing capabilities.</p>
    <p>We teach lessons in our students homes and in our studios. We offer lessons on a variety of instruments. We also provide musicians for performances, events, parties and more. We also have recording and producing capabilities.</p>
    <p><strong>We teach lessons in our students homes and in our studios.</strong> We offer lessons on a variety of instruments. We also provide musicians for performances, events, parties and more. We also have recording and producing capabilities.</p>
  </div>
  <div class="lessons-photo" role="img" aria-label="Photo of a teacher giving a piano lesson to a young student"></div>
</section>

<aside class="side about">
  <h3>About Us</h3>
  <p>I started K.L. Music Studio so we can expand. We teach lessons in our students homes and in our studios. We offer lessons on a variety of instruments.</p>
  <span class="more"></span>
</aside>
<aside class="side news">
  <h3>News &amp; Events</h3>
  <p>I started K.L. Music Studio so we can expand. We teach lessons in our students homes and in our studios. We offer lessons on a variety of instruments.</p>
  <span class="more"></span>
</aside>
<aside class="side watch">
  <div class="watch-video" role="img" aria-label="Video player thumbnail of a lesson recording"></div>
  <div class="watch-info">
    <h3>Online Watch</h3>
    <p>We teach lessons in our students homes and in our studios</p>
  </div>
  <a class="btn" href="#">Click Here</a>
</aside>

<footer class="site-footer">
  <nav><a href="#">Home</a><span>|</span><a href="#">About Us</a><span>|</span><a href="#">Home Lessons</a><span>|</span><a href="#">Events</a><span>|</span><a href="#">Contact Us</a></nav>
  <p>Copyright © 2011. All Rights Reserved.</p>
</footer>
</body>
</html>
```